Single Page website for Product Company

I need a website designed for my small startup company "Lantern Yard Furnishings". We design and manufacture custom innovative indoor/outdoor entertainment furnishings e.g. outdoor TV enclosures, outdoor bars and outdoor kitchens. I'm looking for a single page site based on the the tinyShelf-SoloView-storefront bootstrap page, attached.

I've also attached pictures of my products, these need to be photoshopped and placed in an outdoor patio area if possible.

Target Market(s)

Home owners

Industry/Entity Type

It Company

Coding

Coded - Design and coding required

Number of Pages Required

1 page

Requirements
Must have
• Must be single page site built with attached bootstrap template and adjust to screen size e.g. ipad, mobile phone and computer
Nice to have
• Integration with vendaro

```html
<!DOCTYPE html>
<html lang="en">
<head>
<meta charset="utf-8">
<title>Lantern Yard Furnishings</title>
<link href="https://fonts.googleapis.com/css2?family=Jost:wght@400;500;600&display=swap" rel="stylesheet">
<style>
:root{
  --orange:#f7941d;
  --blue:#3ea4ea;
  --blue-light:#4fb8f5;
  --green:#4cc812;
  --ink:#2b2b2b;
  --muted:#8a8a8a;
  --line:#e2e2e2;
  --panel:#f1f1f1;
  --dark:#151515;
  --white:#ffffff;
}
*{box-sizing:border-box;margin:0;padding:0}
html,body{width:1200px;height:2936px;overflow:hidden}
body{position:relative;font-family:"Jost",Arial,sans-serif;color:var(--ink);background:var(--white)}
.abs{position:absolute}
.btn{position:absolute;display:flex;align-items:center;justify-content:center;color:var(--white);font-size:12px;font-weight:500;text-decoration:none}
.btn--blue{background:var(--blue)}
.btn--orange{background:var(--orange)}
.heading{position:absolute;left:0;width:1200px;text-align:center;font-size:19px;font-weight:500}
.heading::after{content:"";position:absolute;left:584px;top:32px;width:32px;height:2px;background:var(--blue)}

/* hero */
.hero{position:absolute;left:0;top:0;width:1200px;height:509px;background:linear-gradient(180deg,#6f6a66 0%,#8b7f72 45%,#7c776f 75%,#b7b0a7 100%)}
.brand{left:211px;top:40px;display:flex;align-items:center;gap:8px;color:var(--white);font-size:19px;font-weight:500}
.brand__mark{width:14px;height:14px;border:2px solid var(--white)}
.nav{left:581px;top:42px;color:var(--white);font-size:14px}
.nav a{position:absolute;white-space:nowrap;color:var(--white);text-decoration:none}
.nav a.is-active{color:var(--orange)}
.nav a.is-active::before{content:"";position:absolute;left:0;top:-20px;width:100%;height:2px;background:var(--orange)}
.social{display:flex;gap:6px}
.social span{width:22px;height:22px;border-radius:50%;border:1.5px solid var(--white)}
.social span.is-on{background:var(--blue);border-color:var(--blue)}
.hero__title{left:207px;top:234px;color:var(--white);font-size:23px;line-height:30px;font-weight:400;white-space:nowrap}
.hero__title em{font-style:normal;color:var(--orange)}
.arrow{position:absolute;width:28px;height:28px;border-radius:50%;display:flex;align-items:center;justify-content:center}

/* products */
.product__img{left:274px;top:618px;width:368px;height:319px;background:linear-gradient(180deg,#3e5a2a 0%,#5c7a3b 45%,#a07048 70%,#c9b7a0 100%)}
.product__name{left:683px;top:661px;font-size:17px;font-weight:500}
.product__desc{left:683px;top:687px;width:232px;font-size:12px;line-height:16px;color:var(--muted)}
.product__price{left:683px;top:772px;font-size:22px;font-weight:500;color:var(--orange)}

/* shipping */
.ship{left:0;top:980px;width:1200px;height:99px;background:linear-gradient(90deg,#3a9be3,#52bdf6 50%,#3fa6ec)}
.ship__text{left:272px;top:1016px;color:var(--white);font-size:21px}

/* about */
.about__panel{left:0;top:1079px;width:599px;height:421px;background:var(--panel)}
.about__img{left:599px;top:1079px;width:601px;height:421px;background:linear-gradient(180deg,#f2f2f0 0%,#e3e1dc 55%,#b9a58a 75%,#e8e6e2 100%)}
.about__title{left:207px;top:1136px;font-size:20px;font-weight:500}
.about__text{left:207px;top:1198px;width:358px;font-size:12px;line-height:16.4px;color:#6a6a6a}
.about__text p+p{margin-top:16px}

/* order */
.table{left:207px;top:1610px;width:786px;font-size:12px;border-collapse:collapse}
.table th{font-weight:600;text-align:left;height:30px;border-top:1px solid var(--line);border-bottom:1px solid var(--line)}
.table td{height:31px;color:var(--muted);border-bottom:1px solid var(--line)}
.table .num{text-align:right}
.qty{display:inline-flex;justify-content:space-between;align-items:center;width:38px;height:18px;border:1px solid var(--line);padding:0 5px;font-size:11px}
.sub{position:absolute;font-size:14px;font-weight:500;text-align:center}
.field{position:absolute;height:28px;border:1px solid var(--line);font-size:11px;color:#a7a7a7;padding:0 10px;display:flex;align-items:center;justify-content:space-between}
.sum{position:absolute;left:611px;width:382px;font-size:11px;color:var(--muted);display:flex;justify-content:space-between;padding-bottom:8px;border-bottom:1px solid var(--line)}

/* features */
.feature{position:absolute;top:2161px;width:400px;height:176px;color:var(--white);display:flex;flex-direction:column;align-items:center;font-size:15px;font-weight:500}
.feature svg{margin-top:42px;height:56px}
.feature span{margin-top:20px}

/* footer */
.footer{left:0;top:2539px;width:1200px;height:397px;background:var(--dark)}
.footer__img{left:599px;top:2539px;width:601px;height:397px;background:linear-gradient(135deg,#2a2a2a,#3a3835 55%,#1c1c1c)}
.footer__title{position:absolute;color:var(--white);font-size:21px;font-weight:500}
.contact{left:207px;top:2652px;color:var(--white);font-size:13px;line-height:17px}
.contact b{font-weight:600}
.msg-field{position:absolute;left:642px;width:351px;color:var(--white);font-size:11px;border-bottom:1px solid #8a8a8a}
</style>
</head>
<body>

<header class="hero" role="img" aria-label="Rooftop patio with a stone outdoor TV enclosure and planters against a city skyline"></header>
<div class="abs brand"><span class="brand__mark"></span>Lantern Yard Furnishings</div>
<nav class="abs nav">
  <a class="is-active" style="left:0">Product</a>
  <a style="left:86px">About</a>
  <a style="left:165px">Order</a>
  <a style="left:241px">Contact</a>
</nav>
<div class="abs social" style="left:907px;top:40px"><span class="is-on"></span><span></span><span></span></div>
<h1 class="abs hero__title">We design and manufacture custom innovative<br><em>indoor/outdoor</em> entertainment <em>furnishings</em></h1>
<a class="btn btn--blue" style="left:207px;top:317px;width:124px;height:30px">Shop Now</a>
<div class="arrow" style="left:129px;top:278px;border:1.5px solid var(--white)"><svg width="10" height="10" viewBox="0 0 10 10"><path d="M6.5 1.5 3 5l3.5 3.5" fill="none" stroke="#fff" stroke-width="1.6"/></svg></div>
<div class="arrow" style="left:1043px;top:278px;background:var(--orange)"><svg width="10" height="10" viewBox="0 0 10 10"><path d="M3.5 1.5 7 5 3.5 8.5" fill="none" stroke="#fff" stroke-width="1.6"/></svg></div>

<section>
  <h2 class="heading" style="top:546px">Our Products</h2>
  <div class="abs product__img" role="img" aria-label="Brick outdoor TV enclosure on a garden patio beside a pool"></div>
  <h3 class="abs product__name">Outdoor TV enclosures</h3>
  <p class="abs product__desc">Lorem Ipsum is simply dummy text of the printing and typesetting industry. Lorem Ipsum has been the industry's standard dummy text ever since the 1500s</p>
  <div class="abs product__price">$500</div>
  <a class="btn btn--orange" style="left:683px;top:814px;width:112px;height:29px">Shop Now</a>
  <div class="arrow" style="left:686px;top:867px;width:22px;height:22px;border:1.5px solid var(--orange)"><svg width="8" height="8" viewBox="0 0 10 10"><path d="M6.5 1.5 3 5l3.5 3.5" fill="none" stroke="#f7941d" stroke-width="1.8"/></svg></div>
  <div class="arrow" style="left:715px;top:867px;width:22px;height:22px;background:var(--orange)"><svg width="8" height="8" viewBox="0 0 10 10"><path d="M3.5 1.5 7 5 3.5 8.5" fill="none" stroke="#fff" stroke-width="1.8"/></svg></div>
</section>

<section class="abs ship"></section>
<svg class="abs" style="left:210px;top:1010px" width="42" height="42" viewBox="0 0 42 42" fill="none" stroke="#17315a" stroke-width="2"><path d="M16 26 12 22c4-10 12-17 24-18-1 12-8 20-18 24z"/><circle cx="26" cy="16" r="3"/><path d="M13 23l-6 1 5-7 6 0M19 29l-1 6 7-5 0-6M12 30l-5 5M15 33l-3 3M9 27l-3 3"/></svg>
<div class="abs ship__text">Free international shipping only <span style="color:#17315a;font-weight:500">2 days 21:19:10</span></div>
<a class="btn btn--orange" style="left:879px;top:1016px;width:111px;height:29px">Order Now</a>

<section>
  <div class="abs about__panel"></div>
  <div class="abs about__img" role="img" aria-label="Bright living room with floating stairs, a green wall and a wood TV enclosure"></div>
  <h2 class="abs about__title">About Us</h2>
  <div class="abs about__text">
    <p>Lorem Ipsum is simply dummy text of the printing and typesetting industry. Lorem Ipsum has been the industry's standard dummy text ever since the 1500s, when an unknown printer took a galley of type and scrambled it to make a type specimen book. It has survived not only five centuries, but also the leap into electronic.</p>
    <p>typesetting, remaining essentially unchanged. It was popularised in the 1960s with the release of Fontway sheets containing Lorem Ipsum passages, and more recently with desktop publishing software like Quillset Composer including versions of Lorem Ipsum.</p>
  </div>
</section>

<section>
  <h2 class="heading" style="top:1536px">Order Form</h2>
  <table class="abs table">
    <tr><th style="width:247px">Product</th><th style="width:221px">Unit Cost</th><th>Quantity</th><th class="num">Total</th></tr>
    <tr><td>Bed</td><td>$500</td><td><span class="qty">0<small>&#8964;</small></span></td><td class="num">$0</td></tr>
    <tr><td>Nightstand</td><td>$200</td><td><span class="qty">0<small>&#8964;</small></span></td><td class="num">$0</td></tr>
    <tr><td>Hammock</td><td>$700</td><td><span class="qty">0<small>&#8964;</small></span></td><td class="num">$0</td></tr>
  </table>

  <div class="sub" style="left:207px;width:380px;top:1773px">Payment Method</div>
  <div class="sub" style="left:611px;width:382px;top:1773px">Delivery Address</div>
  <div class="field" style="left:207px;top:1806px;width:186px">Card number</div>
  <div class="field" style="left:407px;top:1806px;width:180px">Code</div>
  <div class="field" style="left:207px;top:1847px;width:186px">January<span>&#8964;</span></div>
  <div class="field" style="left:407px;top:1847px;width:180px">2014<span>&#8964;</span></div>
  <div class="sub" style="left:207px;width:380px;top:1892px">Information</div>
  <div class="field" style="left:207px;top:1926px;width:186px">First Name</div>
  <div class="field" style="left:407px;top:1926px;width:180px">Last Name</div>
  <div class="field" style="left:207px;top:1967px;width:380px">Your Email</div>
  <div class="sub" style="left:207px;width:380px;top:2012px">If you have Coupon Code</div>
  <div class="field" style="left:207px;top:2047px;width:302px">Coupon Code</div>
  <a class="btn btn--blue" style="left:509px;top:2047px;width:78px;height:28px">Check !</a>

  <div class="field" style="left:611px;top:1806px;width:382px">Street Address</div>
  <div class="field" style="left:611px;top:1847px;width:382px">City</div>
  <div class="field" style="left:611px;top:1887px;width:382px">Country</div>
  <div class="field" style="left:611px;top:1928px;width:382px">Post Code</div>
  <div class="sub" style="left:611px;width:382px;top:1973px">Order Sumary</div>
  <div class="sum" style="top:2018px"><span>Shipping cost:</span><span>Free</span></div>
  <div class="sum" style="top:2049px;color:var(--ink)"><span style="color:var(--muted)">Total:</span><b>$0.00</b></div>
  <a class="btn btn--blue" style="left:611px;top:2088px;width:382px;height:29px">Order Product</a>
</section>

<section>
  <div class="feature" style="left:0;background:var(--orange)">
    <svg viewBox="0 0 44 56" width="44" fill="none" stroke="#fff" stroke-width="2.4"><circle cx="22" cy="20" r="16"/><circle cx="22" cy="20" r="10"/><path d="M17 20l4 4 7-7M12 33 7 52l8-4 4 7 4-13M32 33l5 19-8-4-4 7"/></svg>
    <span>Quality Guaranteed</span>
  </div>
  <div class="feature" style="left:400px;background:var(--blue)">
    <svg viewBox="0 0 90 56" width="90" fill="#fff"><rect x="20" y="6" width="42" height="34" rx="2"/><path d="M64 16h12l10 12v12H64z"/><circle cx="34" cy="44" r="7" stroke="#3ea4ea" stroke-width="3"/><circle cx="74" cy="44" r="7" stroke="#3ea4ea" stroke-width="3"/><rect x="2" y="12" width="14" height="3"/><rect x="6" y="20" width="10" height="3"/><rect x="0" y="28" width="16" height="3"/></svg>
    <span>Home Delivery</span>
  </div>
  <div class="feature" style="left:800px;background:var(--green)">
    <svg viewBox="0 0 74 56" width="74" fill="none" stroke="#fff" stroke-width="3"><path d="M8 26V16a9 9 0 0 1 18 0v4"/><rect x="2" y="26" width="30" height="26" fill="#fff"/><rect x="28" y="8" width="42" height="28" rx="3"/><path d="M28 16h42" stroke-width="4"/><path d="M52 28h12"/></svg>
    <span>Secure Payment</span>
  </div>
</section>

<section>
  <h2 class="heading" style="top:2376px">Stay in touch</h2>
  <div class="field" style="left:389px;top:2448px;width:327px;height:29px">Enter your email</div>
  <a class="btn btn--blue" style="left:716px;top:2448px;width:94px;height:29px">Subscribe</a>
</section>

<footer>
  <div class="abs footer"></div>
  <div class="abs footer__img" role="img" aria-label="Dimmed close-up of hands typing on a laptop keyboard"></div>
  <div class="arrow" style="left:585px;top:2523px;background:var(--orange)"><svg width="10" height="10" viewBox="0 0 10 10"><path d="M1.5 6.5 5 3l3.5 3.5" fill="none" stroke="#fff" stroke-width="1.6"/></svg></div>
  <h3 class="footer__title" style="left:207px;top:2611px">Contact Us</h3>
  <div class="abs contact">
    <b>Call Us:</b><br>
    <span style="font-size:17px;line-height:22px">+1 (415) 555-0187</span><br>
    <b>hello@lanternyard.example</b><br>
    <div style="height:10px"></div>
    <b>Location:</b><br>
    <b>12 Orchard Lane 45, Fairview</b><br>
    <b>State 30921</b>
  </div>
  <div class="abs social" style="left:207px;top:2791px"><span style="background:var(--orange);border-color:var(--orange)"></span><span></span><span></span></div>
  <div class="abs" style="left:207px;top:2842px;color:var(--white);font-size:12px">© Copyright 2017 Lantern Yard Furnishings.</div>

  <h3 class="footer__title" style="left:642px;top:2589px">Send us Message</h3>
  <div class="msg-field" style="top:2636px;height:27px">Your Name</div>
  <div class="msg-field" style="top:2686px;height:28px">Enter Email</div>
  <div class="msg-field" style="top:2737px;height:82px">Your Message</div>
  <a class="btn btn--blue" style="left:642px;top:2851px;width:70px;height:28px;gap:6px">Send <svg width="11" height="11" viewBox="0 0 12 12"><path d="M1 6 11 1 8 11 6 7z" fill="#fff"/></svg></a>
</footer>

</body>
</html>
```